Commercial and Multifamily informational website

We need a website for our commercial real estate management company. We will manage offices, retail, apartments and others. Here is the brief verbiage: Providing quality commercial and multifamily portfolio management to Landlords, REITs, and financial institutions. 

Industry/Entity Type

Real Estate

Number of Pages Required

2 page

Font styles to use
Sans Serif
Other font styles liked:
• Muli, Garamond

Colors
0555a3
5c5c5c
3176b5
85acd3
474747

Requirements
Must have
• Home page and contact page

```html
<!DOCTYPE html>
<html lang="en">
<head>
<meta charset="utf-8">
<title>Northgate Property Management</title>
<link rel="stylesheet" href="https://fonts.googleapis.com/css2?family=Mulish:wght@400;600;700;800&display=swap">
<style>
:root{
  --brand:#0555a3;
  --brand-mid:#3176b5;
  --brand-soft:#85acd3;
  --ink:#474747;
  --grey:#5c5c5c;
  --panel:#e6e6e6;
  --white:#fff;
}
*{box-sizing:border-box;margin:0;padding:0}
html,body{width:1200px;height:4147px;overflow:hidden}
body{position:relative;font-family:"Mulish",Arial,sans-serif;color:var(--ink);background:var(--white)}
.abs{position:absolute}
svg{display:block}
.icon{stroke:currentColor;fill:none;stroke-width:2}

/* hero */
.hero{left:0;top:0;width:1200px;height:710px;background:linear-gradient(180deg,#8a93a0 0%,#bfc6cf 35%,#8a8070 70%,#5a5a4e 100%)}
.hero-shade{left:0;top:0;width:1200px;height:710px;background:rgba(40,40,40,.25)}
.topbar{left:0;top:0;width:1200px;height:50px;background:rgba(70,70,70,.55);color:#fff;font-size:11px}
.topbar span{position:absolute;top:18px}
.header{left:0;top:50px;width:1200px;height:84px;background:rgba(70,70,70,.55)}
.logo{left:88px;top:66px;color:#fff;font-weight:800;font-size:22px;letter-spacing:.5px;display:flex;align-items:center;gap:10px}
.logo i{width:14px;height:14px;background:#fff;display:block}
.nav{left:640px;top:76px;display:flex;gap:0;color:#fff;font-size:15px;font-weight:600}
.nav a{display:block;padding:0 18px;color:#fff;text-decoration:none;line-height:20px}
.nav .active{border-bottom:3px solid #fff;padding-bottom:16px}
.hero-title{left:250px;top:350px;width:700px;text-align:center;color:#fff;font-size:28px;font-weight:700;line-height:38px;text-shadow:0 2px 6px rgba(0,0,0,.4)}
.btn{display:flex;align-items:center;justify-content:center;color:#fff;font-weight:700;font-size:17px;text-transform:uppercase}
.btn-dark{background:rgba(60,60,60,.75)}
.btn-blue{background:var(--brand)}

/* headings */
.section-title{left:0;width:1200px;text-align:center;color:var(--brand);font-size:34px;font-weight:700}
.rule{height:3px;background:var(--brand)}
.lede{left:165px;top:905px;width:870px;text-align:center;font-size:16px;line-height:21px;font-weight:600;color:#333}

/* search */
.search-label{left:0;top:1050px;width:1200px;text-align:center;font-size:22px;font-weight:600;color:#333}
.search-box{left:202px;top:1112px;width:671px;height:44px;border:1px solid #bbb;display:flex;align-items:center;padding-left:52px;font-size:17px;color:#888}
.search-btn{left:873px;top:1112px;width:125px;height:44px;background:var(--brand-mid);color:#fff;font-size:17px;display:flex;align-items:center;justify-content:center}
.select{height:47px;border:1px solid #bbb;display:flex;align-items:center;font-size:14px;color:#777;padding-left:50px}
.select b{position:absolute;right:0;top:0;width:47px;height:45px;background:var(--grey)}
.range-label{font-size:14px;color:#555}

/* recommended */
.photo{background:linear-gradient(180deg,#a7b7c9,#6d7d91 55%,#4b5563)}
.arrow-btn{background:var(--brand-mid);display:flex;align-items:center;justify-content:center}
.rec-title{left:644px;top:1297px;color:var(--brand);font-size:25px;font-weight:700}
.rec-sub{left:644px;top:1376px;font-size:20px;font-weight:600;color:#333}
.rec-text{left:644px;top:1414px;width:360px;font-size:13px;line-height:17.5px;color:#444}

/* cards */
.card{width:262px;height:368px;background:#fff;box-shadow:0 2px 10px rgba(0,0,0,.2)}
.card .photo{height:243px}
.card h3{margin:12px 0 0 12px;padding-left:10px;border-left:3px solid #333;font-size:18px;font-weight:600;line-height:18px;color:#333}
.feat{display:grid;grid-template-columns:1fr 1fr;row-gap:14px;margin:16px 0 0 12px;font-size:11px;color:#666}
.feat span{display:flex;align-items:center;gap:6px}
.feat i{width:18px;height:10px;background:#777;display:block}
.price{width:262px;height:47px;display:flex}
.price div{flex:1;background:var(--brand-soft);color:#fff;font-size:22px;font-weight:600;display:flex;align-items:center;justify-content:center}
.price b{width:47px;background:var(--brand-mid);display:flex;align-items:center;justify-content:center;margin-left:3px}

/* why */
.why{width:412px;height:116px;background:var(--panel);display:flex;align-items:center}
.why svg{margin:0 30px 0 38px;color:var(--brand-mid)}
.why h4{color:var(--brand-mid);font-size:16px;font-weight:600;margin-bottom:6px}
.why p{font-size:15px;line-height:18px;color:#444;width:300px}
.stats{left:0;top:2776px;width:1200px;height:138px;background:var(--panel)}
.stat{width:240px;text-align:center;color:#444}
.stat svg{margin:0 auto 10px;color:#555}
.stat .pct{font-size:22px;line-height:24px}
.stat .lbl{font-size:22px;line-height:28px}

/* agents */
.agent .photo{width:262px;height:251px;background:linear-gradient(160deg,#8a7a66,#4e4438 60%,#2e2a26)}
.agent h3{margin-top:20px;padding-left:16px;border-left:3px solid #333;font-size:22px;font-weight:600;line-height:22px;color:#333}
.agent .role{margin-top:8px;font-size:14px;color:#333}
.agent .line{display:flex;align-items:center;gap:16px;margin-top:14px;font-size:14px;color:var(--brand-mid)}
.agent .line svg{color:var(--brand-mid)}

/* info band */
.band{left:0;top:3545px;width:1200px;height:249px;background:linear-gradient(90deg,#1f5fb0,#2a6cc0 50%,#1d5aa8)}
.band h2{position:absolute;top:48px;width:1200px;text-align:center;color:#fff;font-size:34px;font-weight:700}
.band-item{display:flex;align-items:center;gap:14px;color:#fff;font-size:23px;line-height:26px}

/* footer */
.footer{left:0;top:3794px;width:1200px;height:353px;background:#575757;color:#fff}
.foot-logo{left:135px;top:3915px;color:#fff;font-weight:800;font-size:22px;display:flex;align-items:center;gap:10px}
.foot-logo i{width:14px;height:14px;background:#fff;display:block}
.social{width:30px;height:30px;border-radius:50%;background:#fff}
.foot-head{font-size:25px;font-weight:600;padding-left:16px;border-left:3px solid #fff;line-height:26px}
.foot-links{font-size:20px;line-height:37px}
.foot-contact{display:flex;align-items:center;gap:14px;font-size:20px;line-height:24px}
.copy{left:0;top:4104px;width:1200px;text-align:center;font-size:16px}
</style>
</head>
<body>

<!-- Hero -->
<div class="abs hero" role="img" aria-label="Photo of a two-storey suburban house with a garage at dusk"></div>
<div class="abs hero-shade"></div>
<div class="abs topbar">
  <span style="left:700px">&#9742;&nbsp; (800) 123-4567</span>
  <span style="left:865px">&#9993;&nbsp; email@example.com</span>
  <span style="left:1025px">Blog</span>
  <span style="left:1128px;top:14px;width:18px;height:18px;border-radius:50%;background:#888"></span>
</div>
<div class="abs header"></div>
<div class="abs logo"><i></i>Northgate Property Management</div>
<nav class="abs nav">
  <a class="active">HOME</a><a>ABOUT</a><a>AGENTS</a><a>SERVICES</a><a>CONTACT</a>
</nav>
<h1 class="abs hero-title">Providing quality commercial and multifamily portfolio management to Landlords, REITs, and financial institutions.</h1>
<div class="abs btn btn-dark" style="left:410px;top:520px;width:165px;height:55px">Know More</div>
<div class="abs btn btn-blue" style="left:620px;top:520px;width:175px;height:55px">Contact Us</div>

<!-- Welcome -->
<h2 class="abs section-title" style="top:792px">WELCOME</h2>
<div class="abs rule" style="left:560px;top:850px;width:80px"></div>
<p class="abs lede">Lorem ipsum dolor sit amet, consectetur adipiscing elit. Mauris luctus diam lectus, quis porttitor velit maximus in. Vestibulum imperdiet est et nibh mattis, nec congue ex posuere. Maecenas id metus luctus, auctor massa et, tincidunt risus. Duis luctus, ipsum ut accumsan tristique, sem lectus dapibus nunc, quis efficitur nunc orci sed diam. Morbi eu felis ipsum.</p>

<!-- Search -->
<div class="abs search-label">Search for Properties</div>
<div class="abs search-box">Search By State...</div>
<svg class="abs icon" style="left:214px;top:1122px;color:#888" width="24" height="24" viewBox="0 0 24 24"><circle cx="12" cy="8" r="5"/><path d="M3 22c1-5 5-7 9-7s8 2 9 7"/></svg>
<div class="abs search-btn">Search</div>
<div class="abs select" style="left:202px;top:1175px;width:166px">Beds<b></b></div>
<div class="abs select" style="left:382px;top:1175px;width:163px">Bath<b></b></div>
<div class="abs select" style="left:558px;top:1175px;width:208px">Property Type<b></b></div>
<svg class="abs" style="left:802px;top:1182px" width="196" height="12" viewBox="0 0 196 12"><rect x="0" y="5" width="196" height="3" fill="#bbb"/><rect x="0" y="5" width="40" height="3" fill="#3176b5"/><circle cx="40" cy="6" r="5" fill="#3176b5"/><circle cx="190" cy="6" r="5" fill="#999"/></svg>
<div class="abs range-label" style="left:820px;top:1202px">$10,000</div>
<div class="abs range-label" style="left:928px;top:1202px">$1,000,000</div>

<!-- Recommended -->
<div class="abs photo" style="left:169px;top:1286px;width:445px;height:262px" role="img" aria-label="Photo of a modern family house lit at dusk"></div>
<div class="abs arrow-btn" style="left:169px;top:1571px;width:41px;height:63px"><svg width="12" height="18" viewBox="0 0 12 18"><path d="M9 2 3 9l6 7" stroke="#fff" stroke-width="2" fill="none"/></svg></div>
<div class="abs photo" style="left:223px;top:1576px;width:90px;height:54px" role="img" aria-label="Thumbnail of a house exterior"></div>
<div class="abs photo" style="left:347px;top:1576px;width:90px;height:54px" role="img" aria-label="Thumbnail of a house exterior"></div>
<div class="abs photo" style="left:465px;top:1576px;width:90px;height:54px" role="img" aria-label="Thumbnail of a house exterior"></div>
<div class="abs arrow-btn" style="left:573px;top:1571px;width:41px;height:63px"><svg width="12" height="18" viewBox="0 0 12 18"><path d="M3 2l6 7-6 7" stroke="#fff" stroke-width="2" fill="none"/></svg></div>
<h2 class="abs rec-title">RECOMMENDED PROPERTIES</h2>
<div class="abs rule" style="left:644px;top:1350px;width:80px"></div>
<h3 class="abs rec-sub">MODERN HOUSES</h3>
<p class="abs rec-text">Lorem ipsum dolor sit amet, consectetur adipiscing elit. Maecenas at nibh neque. Mauris pharetra tristique ante, sed suscipit justo aliquam lobortis. Pellentesque non efficitur nulla, sit amet ultrices diam. Fusce ullamcorper, sapien tristique lacinia dictum, turpis velit varius velit, non lobortis est ligula et justo. Aliquam tempor euismod enim eu consequat. Ut nec fermentum purus. In hac habitasse platea dictumst.</p>
<div class="abs btn btn-blue" style="left:644px;top:1590px;width:172px;height:47px;font-size:14px">Know More</div>
<div class="abs btn" style="left:835px;top:1590px;width:169px;height:47px;font-size:14px;background:var(--grey)">Get Location</div>

<!-- Properties -->
<h2 class="abs" style="left:169px;top:1768px;color:var(--brand);font-size:34px;font-weight:700">Real Estate Properties</h2>
<div class="abs rule" style="left:169px;top:1828px;width:80px"></div>

<div class="abs card" style="left:169px;top:1872px">
  <div class="photo" role="img" aria-label="Photo of a brick house with red roof"></div>
  <h3>MODERN HOUSE</h3>
  <div class="feat"><span><i></i>4000 SQ. FT</span><span><i></i>04 BEDS</span><span><i></i>01 GARAGE</span><span><i></i>04 BATHS</span></div>
</div>
<div class="abs price" style="left:169px;top:2259px"><div>$150,000</div><b><svg class="icon" style="color:#fff" width="24" height="22" viewBox="0 0 24 22"><path d="M12 20 3 11a5 5 0 0 1 9-6 5 5 0 0 1 9 6z"/></svg></b></div>

<div class="abs card" style="left:470px;top:1872px">
  <div class="photo" role="img" aria-label="Photo of a modern white villa"></div>
  <h3>MODERN HOUSE</h3>
  <div class="feat"><span><i></i>4000 SQ. FT</span><span><i></i>03 BEDS</span><span><i></i>01 GARAGE</span><span><i></i>04 BATHS</span></div>
</div>
<div class="abs price" style="left:470px;top:2259px"><div>$150,000</div><b><svg class="icon" style="color:#fff" width="24" height="22" viewBox="0 0 24 22"><path d="M12 20 3 11a5 5 0 0 1 9-6 5 5 0 0 1 9 6z"/></svg></b></div>

<div class="abs card" style="left:771px;top:1872px">
  <div class="photo" role="img" aria-label="Photo of a modern house with glass facade"></div>
  <h3>MODERN HOUSE</h3>
  <div class="feat"><span><i></i>4000 SQ. FT</span><span><i></i>08 BEDS</span><span><i></i>01 GARAGE</span><span><i></i>04 BATHS</span></div>
</div>
<div class="abs price" style="left:771px;top:2259px"><div>$150,000</div><b><svg class="icon" style="color:#fff" width="24" height="22" viewBox="0 0 24 22"><path d="M12 20 3 11a5 5 0 0 1 9-6 5 5 0 0 1 9 6z"/></svg></b></div>

<!-- Why choose -->
<h2 class="abs section-title" style="top:2380px">Why Choose US ?</h2>
<div class="abs rule" style="left:560px;top:2439px;width:80px"></div>
<div class="abs why" style="left:169px;top:2469px">
  <svg class="icon" width="44" height="44" viewBox="0 0 44 44"><circle cx="22" cy="14" r="9"/><path d="M4 42c2-10 9-14 18-14s16 4 18 14z"/></svg>
  <div><h4>Agents</h4><p>Lorem ipsum dolor sit amet, consectetur adipiscing elit.</p></div>
</div>
<div class="abs why" style="left:619px;top:2469px">
  <svg class="icon" width="44" height="44" viewBox="0 0 44 44"><path d="M22 42S8 26 8 17a14 14 0 0 1 28 0c0 9-14 25-14 25z"/><circle cx="22" cy="17" r="5"/></svg>
  <div><h4>Various Locations</h4><p>Lorem ipsum dolor sit amet, consectetur adipiscing elit.</p></div>
</div>
<div class="abs why" style="left:169px;top:2621px">
  <svg class="icon" width="44" height="44" viewBox="0 0 44 44"><rect x="3" y="8" width="24" height="32"/><rect x="27" y="18" width="14" height="22"/><path d="M8 14h4M17 14h4M8 22h4M17 22h4M8 30h4M17 30h4M31 24h6M31 31h6"/></svg>
  <div><h4>View Appartments</h4><p>Lorem ipsum dolor sit amet, consectetur adipiscing elit.</p></div>
</div>
<div class="abs why" style="left:619px;top:2621px">
  <svg class="icon" width="44" height="44" viewBox="0 0 44 44"><path d="M2 22s8-12 20-12 20 12 20 12-8 12-20 12S2 22 2 22z"/><circle cx="22" cy="22" r="6"/><path d="M6 38 38 6"/></svg>
  <div><h4>Privacy &amp; Security</h4><p>Lorem ipsum dolor sit amet, consectetur adipiscing elit.</p></div>
</div>

<!-- Stats -->
<div class="abs stats"></div>
<div class="abs stat" style="left:137px;top:2792px">
  <svg class="icon" width="30" height="34" viewBox="0 0 30 34"><circle cx="15" cy="10" r="8"/><path d="M2 33c1-9 6-12 13-12s12 3 13 12z"/></svg>
  <div class="pct">80%</div><div class="lbl">Satisfied Customers</div>
</div>
<div class="abs stat" style="left:378px;top:2792px">
  <svg width="34" height="34" viewBox="0 0 34 34"><path d="M2 30 13 12l6 9 4-5 9 14z" fill="#555"/></svg>
  <div class="pct">70%</div><div class="lbl">Partners</div>
</div>
<div class="abs stat" style="left:607px;top:2792px">
  <svg class="icon" width="34" height="34" viewBox="0 0 34 34"><rect x="4" y="3" width="26" height="20"/><path d="M9 9h16M9 15h12M12 23l-4 9M22 23l4 9"/></svg>
  <div class="pct">95%</div><div class="lbl">Project Done</div>
</div>
<div class="abs stat" style="left:834px;top:2792px">
  <svg width="34" height="34" viewBox="0 0 34 34"><circle cx="17" cy="17" r="14" fill="#555"/><path d="M17 17V3M17 17l12 7" stroke="#e6e6e6" stroke-width="2"/></svg>
  <div class="pct">65%</div><div class="lbl">Business Plans</div>
</div>

<!-- Agents -->
<h2 class="abs section-title" style="top:2996px">Agents You Can Trust</h2>
<div class="abs rule" style="left:560px;top:3056px;width:80px"></div>

<div class="abs agent" style="left:169px;top:3100px">
  <div class="photo" role="img" aria-label="Portrait photo of agent"></div>
  <h3>JOHN DOE</h3><div class="role">Designer</div>
  <div class="line"><svg class="icon" width="24" height="18" viewBox="0 0 24 18"><rect x="1" y="1" width="22" height="16"/><path d="m1 1 11 9 11-9M1 17l8-8M23 17l-8-8"/></svg>email@example.com</div>
  <div class="line"><svg width="22" height="22" viewBox="0 0 22 22"><path d="M5 2 9 6 7 9c1 3 3 5 6 6l3-2 4 4-3 3C9 19 3 13 2 5z" fill="currentColor"/></svg>(123) 456 789</div>
</div>
<div class="abs agent" style="left:470px;top:3100px">
  <div class="photo" role="img" aria-label="Portrait photo of agent"></div>
  <h3>JOHN DOE</h3><div class="role">Designer</div>
  <div class="line"><svg class="icon" width="24" height="18" viewBox="0 0 24 18"><rect x="1" y="1" width="22" height="16"/><path d="m1 1 11 9 11-9M1 17l8-8M23 17l-8-8"/></svg>email@example.com</div>
  <div class="line"><svg width="22" height="22" viewBox="0 0 22 22"><path d="M5 2 9 6 7 9c1 3 3 5 6 6l3-2 4 4-3 3C9 19 3 13 2 5z" fill="currentColor"/></svg>(123) 456 789</div>
</div>
<div class="abs agent" style="left:771px;top:3100px">
  <div class="photo" role="img" aria-label="Portrait photo of agent"></div>
  <h3>JOHN DOE</h3><div class="role">Designer</div>
  <div class="line"><svg class="icon" width="24" height="18" viewBox="0 0 24 18"><rect x="1" y="1" width="22" height="16"/><path d="m1 1 11 9 11-9M1 17l8-8M23 17l-8-8"/></svg>email@example.com</div>
  <div class="line"><svg width="22" height="22" viewBox="0 0 22 22"><path d="M5 2 9 6 7 9c1 3 3 5 6 6l3-2 4 4-3 3C9 19 3 13 2 5z" fill="currentColor"/></svg>(123) 456 789</div>
</div>

<!-- Info band -->
<section class="abs band" role="img" aria-label="Blue-tinted photo of office towers">
  <h2>Need More Information ?</h2>
</section>
<div class="abs band-item" style="left:188px;top:3672px"><svg width="38" height="38" viewBox="0 0 22 22"><path d="M5 2 9 6 7 9c1 3 3 5 6 6l3-2 4 4-3 3C9 19 3 13 2 5z" fill="#fff"/></svg>(123) 456-789</div>
<div class="abs band-item" style="left:470px;top:3672px"><svg class="icon" style="color:#fff" width="44" height="34" viewBox="0 0 24 18"><rect x="1" y="1" width="22" height="16"/><path d="m1 1 11 9 11-9M1 17l8-8M23 17l-8-8"/></svg>email@example.com</div>
<div class="abs band-item" style="left:762px;top:3666px"><svg class="icon" style="color:#fff" width="34" height="44" viewBox="0 0 34 44"><path d="M17 42S4 26 4 17a13 13 0 0 1 26 0c0 9-13 25-13 25z"/><circle cx="17" cy="17" r="5"/></svg><span>1234 Street Name,<br>City Name</span></div>

<!-- Footer -->
<footer class="abs footer"></footer>
<div class="abs foot-logo"><i></i>Northgate</div>
<div class="abs" style="left:160px;top:3950px;color:#fff;font-size:15px;font-weight:600">Property Management</div>
<div class="abs social" style="left:176px;top:4011px"></div>
<div class="abs social" style="left:223px;top:4011px"></div>
<div class="abs social" style="left:267px;top:4011px"></div>
<div class="abs foot-head" style="left:470px;top:3845px">Pages</div>
<div class="abs foot-links" style="left:503px;top:3892px"><div>Home</div><div>About</div><div>Sevices</div><div>Agents</div></div>
<div class="abs foot-head" style="left:769px;top:3845px">Contact</div>
<div class="abs foot-contact" style="left:785px;top:3892px"><svg class="icon" width="22" height="24" viewBox="0 0 22 24"><circle cx="11" cy="7" r="5"/><path d="M2 23c1-6 5-8 9-8s8 2 9 8z"/></svg><span>1234 Street Name,<br>City Name</span></div>
<div class="abs foot-contact" style="left:785px;top:3972px"><svg width="22" height="22" viewBox="0 0 22 22"><path d="M5 2 9 6 7 9c1 3 3 5 6 6l3-2 4 4-3 3C9 19 3 13 2 5z" fill="#fff"/></svg>(123) 456 789</div>
<div class="abs foot-contact" style="left:785px;top:4017px"><svg class="icon" width="24" height="18" viewBox="0 0 24 18"><rect x="1" y="1" width="22" height="16"/><path d="m1 1 11 9 11-9"/></svg>email@example.com</div>
<div class="abs" style="left:120px;top:4087px;width:960px;height:1px;background:rgba(255,255,255,.4)"></div>
<div class="abs copy" style="color:#fff">Copyright 2017 - All Rights Reserved</div>

</body>
</html>
```